CD cover required for a Brazilian music duo

This is a duo cd which should reflect the spontaneous way of doing brazilian music. We will have 4 pages to fill, as the cd will be a digi pac. We did pics at a brazilian restaurant with lots of beautiful brazilian elements. Basically the ideal would be a duo pic at the front page. Then opening the cd, maybe again a duo pic but putting the duo more on the background. The third page is the image that you see when you get the cd, I think it should be one element of the restaurant and the back cover, maybe a pic of the guitar and my hand. We need to design the cd itself as well. It is important to transmit a relaxed atmosphere for the cd. We are Brazilians doing music in Germany and people get mostly excited about the relaxed and spontaneous way of being. Music which makes fun to hear, but where we have fun as well. Also important: this is not my solo cd as a singer, but a duo cd. The pics show this as well

Target Market(s)

Audience in our concerts but CD will also be sold in other places

Requirements
Must have
• Pls use pics from the link at the document
Nice to have
• To transport the relaxed atmosphere when we are playing

```html
<!DOCTYPE html>
<html lang="pt">
<head>
<meta charset="utf-8">
<title>Maré Mansa – CD disc labels</title>
<link rel="stylesheet" href="https://fonts.googleapis.com/css2?family=Open+Sans:wght@400;600&display=swap">
<style>
  :root {
    --page-bg: #ffffff;
    --title-white: #ffffff;
    --credit-white: #ffffff;
    --hole-white: #ffffff;
    --ring-yellow: #fff135;
    --ribbon-blue: #1f93c4;
    --ribbon-blue-deep: #1577a8;
    --photo-light: #8a8a8a;
    --photo-dark: #141414;
  }
  html, body {
    margin: 0;
    padding: 0;
    width: 1200px;
    height: 1140px;
    overflow: hidden;
    background: var(--page-bg);
  }
  .disc-sheet {
    display: block;
    width: 1200px;
    height: 1140px;
  }
  .album-title {
    font-family: "Open Sans", Arial, sans-serif;
    font-weight: 600;
    font-size: 44px;
    fill: var(--title-white);
    letter-spacing: 2px;
  }
  .duo-credit {
    font-family: "Open Sans", Arial, sans-serif;
    font-weight: 400;
    font-size: 15px;
    fill: var(--credit-white);
  }
  .spindle-hole { fill: var(--hole-white); }
  .spindle-ring { fill: var(--hole-white); stroke: var(--ring-yellow); stroke-width: 5; }
</style>
</head>
<body>
<svg class="disc-sheet" viewBox="0 0 1200 1140" xmlns="http://www.w3.org/2000/svg">
  <defs>
    <clipPath id="disc-front-clip"><circle cx="600" cy="305" r="243"/></clipPath>
    <clipPath id="disc-back-clip"><circle cx="600" cy="835" r="243"/></clipPath>
    <linearGradient id="ribbon-tones" x1="0" y1="0" x2="1" y2="0">
      <stop offset="0" stop-color="#4a3a5e"/>
      <stop offset="0.2" stop-color="#2f7f6a"/>
      <stop offset="0.4" stop-color="#6b4b8c"/>
      <stop offset="0.55" stop-color="#3e8fb0"/>
      <stop offset="0.75" stop-color="#5f8a3a"/>
      <stop offset="1" stop-color="#7a3c4a"/>
    </linearGradient>
    <linearGradient id="blue-tint" x1="0" y1="0" x2="0" y2="1">
      <stop offset="0" stop-color="#1f93c4"/>
      <stop offset="1" stop-color="#1577a8"/>
    </linearGradient>
    <radialGradient id="duo-photo-tones" cx="0.6" cy="0.35" r="0.8">
      <stop offset="0" stop-color="#8a8a8a"/>
      <stop offset="0.6" stop-color="#3a3a3a"/>
      <stop offset="1" stop-color="#141414"/>
    </radialGradient>
  </defs>

  <g class="disc disc-front" clip-path="url(#disc-front-clip)">
    <rect class="ribbon-photo" x="357" y="62" width="486" height="246" fill="url(#ribbon-tones)"
          role="img" aria-label="Photograph of many colourful wish ribbons hanging side by side"/>
    <rect class="ribbon-blue-band" x="357" y="308" width="486" height="240" fill="url(#blue-tint)"
          role="img" aria-label="The same hanging ribbons tinted in blue"/>
  </g>
  <circle class="spindle-ring" cx="600" cy="305" r="32"/>
  <text class="album-title" x="600" y="428" text-anchor="middle">MARÉ MANSA</text>
  <text class="duo-credit" x="600" y="454" text-anchor="middle">Mariana Costa &amp; Rafael Teixeira</text>

  <g class="disc disc-back" clip-path="url(#disc-back-clip)">
    <rect class="duo-photo" x="357" y="592" width="486" height="486" fill="url(#duo-photo-tones)"
          role="img" aria-label="Black and white photograph of the duo: a guitarist playing beside a singer with long curly hair, in front of floral wallpaper"/>
  </g>
  <circle class="spindle-hole" cx="600" cy="835" r="30"/>
  <text class="album-title" x="600" y="994" text-anchor="middle">MARÉ MANSA</text>
  <text class="duo-credit" x="600" y="1018" text-anchor="middle">Mariana Costa &amp; Rafael Teixeira</text>
</svg>
</body>
</html>
```